Need Modern Elegant Professional Invoice Design

Need modern elegant professional invoice design along with a second page for time and expense log for professional services

```html
<!DOCTYPE html>
<html lang="en">
<head>
<meta charset="utf-8">
<title>Vantage Adjusters – Invoice</title>
<link rel="stylesheet" href="https://fonts.googleapis.com/css2?family=Barlow:wght@400;500;600;700&display=swap">
<style>
  :root {
    --indigo: #3b2c85;
    --orange: #ef7a1f;
    --ink: #1c1c1c;
    --rule: #b9b9b9;
    --paper: #ffffff;
    --backdrop: #f3f3f3;
  }
  * { margin: 0; padding: 0; box-sizing: border-box; }
  html, body { width: 1200px; height: 1200px; overflow: hidden; }
  body { background: var(--backdrop); font-family: "Barlow", sans-serif; color: var(--ink); position: relative; }

  .sheet { position: absolute; left: 224px; top: 71px; width: 755px; height: 1067px; background: var(--paper); overflow: hidden; }
  .sheet-shapes { position: absolute; inset: 0; }
  .abs { position: absolute; white-space: nowrap; }

  .brand-name { left: 76px; top: 104px; font-size: 31px; font-weight: 700; color: var(--orange); line-height: 1; }

  .invoice-title { left: 466px; top: 172px; font-size: 37px; font-weight: 700; color: var(--orange); letter-spacing: 0.5px; line-height: 1; }
  .meta { font-size: 15.5px; font-weight: 500; line-height: 18.5px; top: 220px; }
  .meta-labels { left: 466px; }
  .meta-values { left: 578px; }

  .party-tag { font-size: 13.5px; font-weight: 700; color: var(--orange); text-align: right; line-height: 17px; top: 204px; }
  .party-tag.bill { left: 74px; width: 32px; }
  .party-tag.ship { left: 252px; width: 34px; }
  .party-lines { font-size: 14.5px; font-weight: 500; line-height: 17px; top: 202px; }
  .party-lines.bill { left: 112px; }
  .party-lines.ship { left: 293px; }

  .th { top: 310px; font-size: 12.5px; font-weight: 600; color: #fff; text-align: center; }
  .th.st { left: 98px; font-size: 15px; top: 308px; }

  .totals { left: 466px; top: 596px; font-size: 15.5px; font-weight: 700; line-height: 19px; }
  .total-label { left: 476px; top: 671px; font-size: 15.5px; font-weight: 700; color: #fff; }

  .section-title { left: 74px; font-size: 17px; font-weight: 600; color: var(--orange); }
  .section-body { left: 74px; font-size: 15px; font-weight: 500; line-height: 18.5px; }
  .pay-title { top: 703px; }
  .pay-body { top: 727px; }
  .pay-body span { display: inline-block; }
  .terms-title { top: 804px; }
  .terms-body { top: 828px; font-size: 15.5px; }

  .contact { top: 916px; font-size: 14px; font-weight: 500; line-height: 17px; }
  .contact.phone { left: 115px; }
  .contact.web { left: 353px; }
  .contact.place { left: 567px; }
  .icon { position: absolute; }

  .footer-name { left: 80px; top: 1018px; font-size: 23px; font-weight: 700; color: #fff; line-height: 1; }
</style>
</head>
<body>
<main class="sheet">
  <svg class="sheet-shapes" width="755" height="1067" viewBox="0 0 755 1067">
    <polygon points="456,0 755,0 755,96 524,96" fill="var(--indigo)"/>
    <rect x="324" y="297" width="360" height="41" fill="var(--indigo)"/>
    <polygon points="78,294 324,294 362,342 78,342" fill="var(--orange)"/>
    <g stroke="var(--rule)" stroke-width="0.8">
      <line x1="160" y1="342" x2="160" y2="573"/>
      <line x1="345" y1="338" x2="345" y2="573"/>
      <line x1="455" y1="338" x2="455" y2="573"/>
      <line x1="565" y1="338" x2="565" y2="573"/>
      <line x1="87" y1="386" x2="673" y2="386"/>
      <line x1="87" y1="433" x2="673" y2="433"/>
      <line x1="87" y1="477" x2="673" y2="477"/>
      <line x1="87" y1="523" x2="673" y2="523"/>
      <line x1="87" y1="573" x2="673" y2="573"/>
    </g>
    <line x1="446" y1="638" x2="656" y2="638" stroke="var(--ink)" stroke-width="1.4"/>
    <rect x="451" y="662" width="125" height="36" fill="var(--indigo)"/>
    <polygon points="538,658 683,658 683,701 570,701" fill="var(--orange)"/>
    <polygon points="326,1022 581,1022 613,1067 350,1067" fill="var(--orange)"/>
    <polygon points="0,982 298,982 358,1067 0,1067" fill="var(--indigo)"/>
  </svg>

  <div class="abs brand-name">VANTAGE ADJUSTERS</div>

  <h1 class="abs invoice-title">INVOICE</h1>
  <div class="abs meta meta-labels">Invoice:<br>Invoice Date:<br>Customer ID:</div>
  <div class="abs meta meta-values">656154<br>01 January 2021<br>00001</div>

  <div class="abs party-tag bill">BILL<br>TO</div>
  <div class="abs party-lines bill">Name<br>Street Address<br>Address 2<br>City, ST&nbsp; ZIP Code</div>
  <div class="abs party-tag ship">SHIP<br>TO</div>
  <div class="abs party-lines ship">Name<br>Street Address<br>Address 2<br>City, ST&nbsp; ZIP Code</div>

  <div class="abs th st">ST</div>
  <div class="abs th" style="left:183px;">ITEM DESCRIPTION</div>
  <div class="abs th" style="left:384px;">RATE</div>
  <div class="abs th" style="left:492px;">QTY</div>
  <div class="abs th" style="left:598px;">AMOUNT</div>

  <div class="abs totals">SUBTOTAL<br>TAX VAT 15%</div>
  <div class="abs total-label">TOTAL</div>

  <h2 class="abs section-title pay-title">PAYMENT METHOD</h2>
  <div class="abs section-body pay-body"><span style="min-width:80px">ACCOUNT:</span> 00000123<br><span style="min-width:62px">SWIFT:</span> 123456789<br><span style="min-width:70px">PAYPAL:</span> YOURNAME@MAILBOX.COM</div>
  <h2 class="abs section-title terms-title">TERMS &amp; CONDITIONS/NOTES</h2>
  <div class="abs section-body terms-body">LOREM IPSUM DOLER SIT AMET, CONSECTETUER<br>ADIPINCING ELIT, DED DIAM NINMUMMY NIBH</div>

  <svg class="icon" style="left:77px;top:922px" width="26" height="26" viewBox="0 0 24 24">
    <path fill="var(--indigo)" d="M6.6 10.8a15.1 15.1 0 0 0 6.6 6.6l2.2-2.2a1 1 0 0 1 1-.25 11.4 11.4 0 0 0 3.6.57 1 1 0 0 1 1 1V20a1 1 0 0 1-1 1A17 17 0 0 1 3 4a1 1 0 0 1 1-1h3.5a1 1 0 0 1 1 1c0 1.25.2 2.45.57 3.57a1 1 0 0 1-.25 1z"/>
  </svg>
  <div class="abs contact phone">+000 12345 6789<br>+000 12345 6789</div>

  <svg class="icon" style="left:316px;top:921px" width="28" height="28" viewBox="0 0 28 28" fill="none" stroke="var(--indigo)" stroke-width="1.6">
    <circle cx="14" cy="14" r="12"/>
    <ellipse cx="14" cy="14" rx="5.5" ry="12"/>
    <line x1="2" y1="14" x2="26" y2="14"/>
    <path d="M4 8h20M4 20h20"/>
  </svg>
  <div class="abs contact web">info@vantageadj.com<br>www.vantageadj.com</div>

  <svg class="icon" style="left:543px;top:922px" width="18" height="26" viewBox="0 0 18 26">
    <path fill="var(--indigo)" d="M9 0a9 9 0 0 0-9 9c0 6.8 9 17 9 17s9-10.2 9-17a9 9 0 0 0-9-9zm0 13a4 4 0 1 1 0-8 4 4 0 0 1 0 8z"/>
  </svg>
  <div class="abs contact place">123 street address<br>city here - 123</div>

  <div class="abs footer-name">VANTAGE ADJUSTERS</div>
</main>
</body>
</html>
```